Stage Design Company Business Card

We are looking to step up up our business card design for our team.

We are a Full service Design and Consultation company for Stage and TV with an emphasis in Theatrical Lighting.

We like our materials to be clean and modern with solid colors free of patterns and gradients. Our brand consists of 4 primary colors Purple, Black, Grey, and White. Provided is our Word Mark as well as our Symbol Logo.

We would like our cards to leave an impression beyond the information, show our attention to design and detail, and make our marks an easily recognized feature (together or apart) for our clients.

We need a warm approachable comfortable feel for some clients, and a professional flair for the board member type clients.

Attached are our brand elements, and our existing cards to give a sense of our style and a glipse at the information we provide on our cards.

Target Market(s)

broad client base from church leaders to high school teachers and architects.

Industry/Entity Type

Business

Contact Information for Business Card

We format our phone number with periods not parenthesis or dashes. Information will be edited for each of our team members, and team member specific cards are not part of this scope, but rather a template so to speak.

Font styles to use
Sans Serif

Colors
6b449b
ffffff
000000
333333
aaaaaa

Requirements
Must have
• Wordmark and logo mark present (does not need to exist on the same side of card)
• Brand Colors,
• Name, Phone, Email, Address.
• Unique choices that make someone stop and take a second look
Nice to have
• It would be nice to somehow convey what we DO, as our brand name does not lend itself to this, outside of an obvious tagline though.....
• social media if not crowded. all of our handles match (instagram, twitter, facebook)
Should not have
• "clipart"

```html
<!DOCTYPE html>
<html lang="en">
<head>
<meta charset="utf-8">
<title>Halvern Entertainment – Business Card</title>
<link rel="stylesheet" href="https://fonts.googleapis.com/css2?family=Roboto:wght@300;400;500&family=Roboto+Condensed:wght@400;700&display=swap">
<style>
  :root {
    --page-bg: #d6d6d6;
    --brand-purple: #2e2966;
    --brand-purple-soft: #443c7a;
    --card-white: #ffffff;
    --text-light: #ececf4;
    --shadow: rgba(0, 0, 0, 0.18);
  }
  * { box-sizing: border-box; margin: 0; padding: 0; }
  html, body {
    width: 1200px; height: 1200px; overflow: hidden;
    background: var(--page-bg);
  }
  .card {
    position: absolute; left: 170px;
    width: 839px; height: 475px;
    overflow: hidden;
    box-shadow: 0 10px 30px var(--shadow);
  }

  /* Front side */
  .card-front { top: 40px; background: var(--brand-purple); color: var(--text-light); font-family: "Roboto Condensed", sans-serif; }
  .identity { position: absolute; left: 62px; top: 58px; display: flex; align-items: center; gap: 28px; }
  .identity-mark { width: 60px; height: 60px; border-radius: 50%; background: var(--text-light); }
  .person-name { font-size: 41px; font-weight: 700; letter-spacing: 0.5px; line-height: 1; }
  .person-title { font-size: 22px; font-weight: 400; margin-top: 10px; margin-left: 3px; }
  .contact-list { position: absolute; left: 70px; top: 200px; list-style: none; }
  .contact-item { display: flex; align-items: flex-start; height: 50px; font-size: 23px; line-height: 28px; }
  .contact-item svg { width: 22px; height: 22px; margin-top: 3px; margin-right: 12px; flex: none; }
  .contact-phone { letter-spacing: 5px; }
  .contact-address { height: 60px; }

  /* Back side */
  .card-back { top: 645px; background: var(--card-white); color: var(--brand-purple); font-family: "Roboto", sans-serif; }
  .company-name { position: absolute; left: 0; right: 0; top: 140px; text-align: center; font-size: 54px; font-weight: 500; letter-spacing: 30px; text-indent: 30px; line-height: 1; }
  .company-type { position: absolute; left: 0; right: 0; top: 212px; text-align: center; font-size: 17px; font-weight: 300; letter-spacing: 21px; text-indent: 21px; }
  .tagline-band { position: absolute; left: 0; top: 292px; width: 839px; height: 30px; }
  .tagline { position: absolute; left: 0; right: 0; top: 292px; text-align: center; font-size: 27px; font-weight: 300; line-height: 30px; }
  .services { position: absolute; left: 180px; top: 372px; display: flex; align-items: center; }
  .service { display: flex; align-items: center; font-size: 20px; font-weight: 400; }
  .service svg { width: 66px; height: 56px; margin-right: 28px; }
  .service + .service { margin-left: 34px; }
</style>
</head>
<body>

<section class="card card-front" aria-label="Card front">
  <div class="identity">
    <span class="identity-mark" aria-hidden="true"></span>
    <div>
      <h1 class="person-name">MARCUS L REED</h1>
      <p class="person-title">Founder/Director</p>
    </div>
  </div>
  <ul class="contact-list">
    <li class="contact-item contact-phone">
      <svg viewBox="0 0 24 24" aria-hidden="true"><path fill="none" stroke="currentColor" stroke-width="1.8" d="M9 3 L6 4 Q3 12 9 21 L12 20 L10 15 L8 15 Q6 11 8 8 L10 8 Z"/></svg>
      480.555.0143
    </li>
    <li class="contact-item">
      <svg viewBox="0 0 24 24" aria-hidden="true"><circle cx="12" cy="12" r="4" fill="none" stroke="currentColor" stroke-width="2"/><path d="M16 8 V14 Q16 17 19 16 Q22 14 21 10 A9.5 9.5 0 1 0 16 20" fill="none" stroke="currentColor" stroke-width="2"/></svg>
      MARCUS@HALVERN-E.COM
    </li>
    <li class="contact-item">
      <svg viewBox="0 0 24 24" aria-hidden="true"><g fill="none" stroke="currentColor" stroke-width="1.3"><circle cx="12" cy="12" r="10"/><ellipse cx="12" cy="12" rx="4.5" ry="10"/><path d="M2 12 H22 M4 6.5 H20 M4 17.5 H20"/></g></svg>
      www.halvern-e.com
    </li>
    <li class="contact-item contact-address">
      <svg viewBox="0 0 24 24" aria-hidden="true"><path fill="currentColor" d="M12 1 A7 7 0 0 1 19 8 Q19 13 12 23 Q5 13 5 8 A7 7 0 0 1 12 1 Z"/></svg>
      <span>214 N ORCHARD AVE TEMPE,<br>AZ 85281</span>
    </li>
  </ul>
</section>

<section class="card card-back" aria-label="Card back">
  <h2 class="company-name">HALVERN</h2>
  <p class="company-type">ENTERTAINMENT</p>

  <svg class="tagline-band" viewBox="0 0 839 30" aria-hidden="true">
    <defs>
      <linearGradient id="band-left" x1="0" x2="1"><stop offset="0" stop-color="#2e2966"/><stop offset="1" stop-color="#2e2966" stop-opacity="0"/></linearGradient>
      <linearGradient id="band-right" x1="1" x2="0"><stop offset="0" stop-color="#2e2966"/><stop offset="1" stop-color="#2e2966" stop-opacity="0"/></linearGradient>
    </defs>
    <g fill="url(#band-left)"><rect x="0" y="1" width="220" height="2"/><rect x="0" y="9" width="220" height="2"/><rect x="0" y="17" width="220" height="2"/><rect x="0" y="25" width="220" height="2"/></g>
    <g fill="url(#band-right)"><rect x="619" y="1" width="220" height="2"/><rect x="619" y="9" width="220" height="2"/><rect x="619" y="17" width="220" height="2"/><rect x="619" y="25" width="220" height="2"/></g>
  </svg>
  <p class="tagline">DESIGN AND CONSULTATION</p>

  <div class="services">
    <div class="service">
      <svg viewBox="0 0 66 56" aria-hidden="true"><g fill="none" stroke="currentColor" stroke-width="2.4"><rect x="2" y="2" width="62" height="38"/><path d="M2 8 Q16 8 12 34 M64 8 Q50 8 54 34 M12 34 H54"/><path d="M3 54 V49 A7 7 0 0 1 17 49 V54 Z M25 54 V49 A7 7 0 0 1 39 49 V54 Z M47 54 V49 A7 7 0 0 1 61 49 V54 Z"/></g></svg>
      STAGE
    </div>
    <div class="service">
      <svg viewBox="0 0 66 56" aria-hidden="true"><g fill="none" stroke="currentColor" stroke-width="2.4"><rect x="2" y="2" width="62" height="40" rx="2"/><circle cx="33" cy="22" r="11"/><path d="M33 42 V52 M22 53 H44"/></g></svg>
      TV
    </div>
    <div class="service">
      <svg viewBox="0 0 66 56" aria-hidden="true"><path d="M8 4 L36 44 H28 Z M58 4 L30 44 H38 Z" fill="currentColor" opacity="0.35"/><path d="M14 40 H52 L60 54 H6 Z" fill="none" stroke="currentColor" stroke-width="2.4"/><path d="M4 2 L12 8 M62 2 L54 8" stroke="currentColor" stroke-width="5"/></svg>
      LIGHTING
    </div>
  </div>
</section>

</body>
</html>
```